R&K Security Services PTY. LTD.

Ive just had my logo made and I'm looking for some simple but strong designs for my business cards the company is a security company.

Please use dark colors.

Regards,

Dale Prentiss

Reason: Need more time for discussion with other directors

Industry/Entity Type

Security

Font styles to use
Sans Serif
Decorative

```html
<!DOCTYPE html>
<html lang="en">
<head>
<meta charset="utf-8">
<title>R&amp;K Security Services – Business Card</title>
<link rel="stylesheet" href="https://fonts.googleapis.com/css2?family=Cinzel:wght@400&family=Libre+Baskerville:wght@700&family=Oswald:wght@300&display=swap">
<style>
  :root {
    --page: #ececec;
    --card: #ffffff;
    --ink: #1b1b1b;
    --grey: #6a6a6a;
    --rule: #2b2b2b;
  }
  * { box-sizing: border-box; margin: 0; padding: 0; }
  html, body { width: 1166px; height: 1200px; overflow: hidden; background: var(--page); }
  .sheet { position: relative; width: 1166px; height: 1200px; }

  .card {
    position: absolute; left: 133px; width: 900px; height: 514px;
    background: var(--card);
    box-shadow: 0 6px 22px rgba(0,0,0,.12);
  }
  .card--front { top: 50px; }
  .card--back  { top: 636px; }

  /* brand name block standing in for the mark */
  .brand {
    position: absolute; display: flex; align-items: center; gap: 14px;
    font-family: "Cinzel", serif; font-weight: 400; color: var(--ink);
    letter-spacing: 2px; line-height: 1.15;
  }
  .brand__dot { width: 22px; height: 22px; border-radius: 50%; background: var(--ink); flex: none; }
  .card--front .brand { right: 60px; top: 150px; font-size: 24px; width: 250px; }
  .card--back .brand {
    left: 285px; width: 330px; top: 50%; transform: translateY(-50%);
    justify-content: center; font-size: 32px;
  }

  /* name */
  .person { position: absolute; left: 70px; top: 110px; text-align: center; }
  .person__name {
    font-family: "Cinzel", serif; font-weight: 400; font-size: 42px; color: var(--ink); letter-spacing: 2px;
  }
  .person__role {
    margin-top: 6px; font-family: "Oswald", sans-serif; font-weight: 300;
    font-size: 13px; letter-spacing: 3px; color: var(--grey);
  }

  /* contacts */
  .contacts { position: absolute; left: 70px; top: 235px; list-style: none; }
  .contacts__item {
    display: flex; align-items: center; gap: 12px; margin-bottom: 10px;
    font-family: "Oswald", sans-serif; font-weight: 300; font-size: 17px; color: var(--grey);
    letter-spacing: .5px;
  }
  .contacts__icon {
    width: 22px; height: 22px; background: var(--ink); display: flex;
    align-items: center; justify-content: center; border-radius: 2px;
  }

  /* address band */
  .address { position: absolute; left: 60px; right: 60px; top: 360px; height: 120px; }
  .address__rule { position: absolute; left: 0; width: 100%; height: 12px; }
  .address__rule--top { top: 0; }
  .address__rule--bottom { bottom: 0; }
  .address__flourish {
    position: absolute; left: 50%; top: 24px; transform: translateX(-50%);
    width: 190px; height: 32px;
    background: linear-gradient(90deg, rgba(120,120,120,0), #8c8c8c 50%, rgba(120,120,120,0));
    opacity: .55; border-radius: 16px;
  }
  .address__text {
    position: absolute; left: 0; right: 0; top: 70px; text-align: center;
    font-family: "Libre Baskerville", serif; font-weight: 700; font-size: 19px; color: var(--ink);
  }

  /* back card rules: plain lines */
  .back-rule { position: absolute; width: 200px; height: 0; border-top: 2px solid var(--rule); }
  .back-rule--left { left: 60px; top: 400px; }
  .back-rule--right { right: 60px; top: 290px; }
</style>
</head>
<body>
<main class="sheet">

  <section class="card card--front" aria-label="Card front">
    <div class="person">
      <h1 class="person__name">DALE PRENTISS</h1>
      <p class="person__role">- OWNER -</p>
    </div>

    <ul class="contacts">
      <li class="contacts__item">
        <span class="contacts__icon">
          <svg width="14" height="10" viewBox="0 0 14 10"><rect x="0.5" y="0.5" width="13" height="9" fill="none" stroke="#fff"/><path d="M0.5 0.5 L7 6 L13.5 0.5" fill="none" stroke="#fff"/></svg>
        </span>
        DALE@RKSECURITY.NET.AU
      </li>
      <li class="contacts__item">
        <span class="contacts__icon">
          <svg width="8" height="14" viewBox="0 0 8 14"><rect x="0.5" y="0.5" width="7" height="13" rx="1" fill="none" stroke="#fff"/><circle cx="4" cy="11" r="0.9" fill="#fff"/></svg>
        </span>
        0412 555 019
      </li>
      <li class="contacts__item">
        <span class="contacts__icon">
          <svg width="14" height="12" viewBox="0 0 14 12"><path d="M1 4 Q7 0 13 4 L11 6 L9 4.5 L5 4.5 L3 6 Z" fill="#fff"/><rect x="3" y="7" width="8" height="4" fill="#fff"/></svg>
        </span>
        (03) 9555 0148
      </li>
    </ul>

    <div class="brand"><span class="brand__dot"></span><span>R&amp;K Security Services</span></div>

    <div class="address">
      <svg class="address__rule address__rule--top" viewBox="0 0 780 12" preserveAspectRatio="none">
        <line x1="8" y1="6" x2="772" y2="6" stroke="var(--rule)" stroke-width="2"/>
        <circle cx="5" cy="6" r="4" fill="none" stroke="var(--rule)" stroke-width="1.5"/>
        <circle cx="775" cy="6" r="4" fill="none" stroke="var(--rule)" stroke-width="1.5"/>
      </svg>
      <div class="address__flourish" role="img" aria-label="Ornamental scroll flourish"></div>
      <p class="address__text">P.O. Box 7 Hollowmere Victoria 3999</p>
      <svg class="address__rule address__rule--bottom" viewBox="0 0 780 12" preserveAspectRatio="none">
        <line x1="0" y1="3" x2="780" y2="3" stroke="var(--rule)" stroke-width="1"/>
        <line x1="0" y1="8" x2="780" y2="8" stroke="var(--rule)" stroke-width="3"/>
      </svg>
    </div>
  </section>

  <section class="card card--back" aria-label="Card back">
    <div class="back-rule back-rule--left"></div>
    <div class="brand"><span class="brand__dot"></span><span>R&amp;K Security Services</span></div>
    <div class="back-rule back-rule--right"></div>
  </section>

</main>
</body>
</html>
```